Stationary Design for Quince consultant and support company

We need new stationary designed for a London based support company that provide on-site and remote support services for Quince products. Our clients are both consumers and businesses.

We would like a letterhead, compliment slip, business card and possibly an e-mail signature designed.

Business card designs can be either 1 side or 2, depending on designs we receive we may choose a preference for 1 or 2 sides later on in the design stage.

Designs needs to be at least 300dpi and should be done using CMYK colours.

We want the design to be bold, easy to read, clean and professional.

We have attached our company logo in 2 colour variations (if you need any other source files then please ask).

Our logo colours are as follows:

Blue (85, 50, 0, 0) and Green (50, 0, 100, 0)

We use two different suppliers for out stationary so here are the size dimensions for both. Unfortunately they are ever so slightly different size wise so hopefully we can get something that accommodates both, we can provide dimensions if required for final versions.

Some fonts that have been used before with our company are Probert (for tagline on our company logo) and previously had Nauman used, however we are very much open to seeing what the designers come up with and the fonts mentioned are not a requirement.
Updates

Company details for designs (however the template should be editable for multiple staff) Vorn-Q Ltd. Registered Office: 62-74 Marrow Lane London N7 3QT 020 7195 8843 www.vorn-q.co info@vorn-q.co Company is Registered in England and Wales Company No. 06412853 Directors details (if you want to make the template using his details), rest of the details are as above Dan Myles Director dan@vorn-q.co

Hi all, Thank you for your submissions so far. Could we please ask that you don't use the logo with the tagline from our website for the stationary designs and only the logos provided in the design brief. For the business cards we are looking at normal rectangular business cards to be used and we can provide a template guide for size if needed, please just ask. Regards Vorn-Q Team

Target Market(s)

Our target market are consumers (of all ages) and small/medium businesses.

Industry/Entity Type

Business

Font styles to use
Serif
Sans Serif

Requirements
Must have
• At least business card, letterhead and compliment slip submitted (we need all 3 designed this time round)
Should not have
• Business cards should not have the writing "registered office" (letterheads and compliment slips can along the bottom edge)

```html
<!DOCTYPE html>
<html lang="en">
<head>
<meta charset="utf-8">
<title>Vorn-Q Stationery</title>
<link href="https://fonts.googleapis.com/css2?family=Source+Sans+3:wght@400;600;700&family=Cormorant+Garamond:ital,wght@1,500&display=swap" rel="stylesheet">
<style>
  :root {
    --backdrop: #a7a7a7;
    --paper: #ffffff;
    --ink: #2b2b2b;
    --ink-soft: #555555;
    --charcoal: #231f20;
    --brand-blue: #2a8fd0;
    --brand-green: #8dc63f;
    --sans: "Source Sans 3", "Helvetica Neue", Arial, sans-serif;
    --script: "Cormorant Garamond", Georgia, serif;
  }
  * { box-sizing: border-box; margin: 0; padding: 0; }
  html, body { width: 1200px; height: 670px; overflow: hidden; }
  body { background: var(--backdrop); font-family: var(--sans); color: var(--ink); position: relative; }

  .sheet { position: absolute; background: var(--paper); box-shadow: 0 2px 6px rgba(0,0,0,.25); overflow: hidden; }

  .wordmark { position: absolute; font-family: var(--sans); font-weight: 700; color: var(--ink); letter-spacing: .02em; white-space: nowrap; display: flex; align-items: center; gap: .25em; line-height: 1; }
  .wordmark .mark-square { width: .42em; height: .42em; background: var(--brand-green); display: inline-block; }
  .wordmark--light { color: var(--paper); }

  .brand-bar { position: absolute; left: 0; right: 0; bottom: 0; display: flex; gap: 3px; }
  .brand-bar span { display: block; height: 100%; }
  .brand-bar .bar-dark { flex: 2.55; background: var(--charcoal); }
  .brand-bar .bar-blue { flex: 1; background: var(--brand-blue); }
  .brand-bar .bar-green { flex: 1; background: var(--brand-green); }

  .contact { position: absolute; font-size: 4.2px; line-height: 5.2px; color: var(--ink-soft); }
  .contact-row { display: flex; gap: 3px; align-items: flex-start; }
  .contact-row svg { flex: none; margin-top: .3px; }

  /* Business card front */
  .card-front { left: 106px; top: 331px; width: 221px; height: 127px; }
  .card-front .wordmark { right: 14px; top: 18px; font-size: 14px; }
  .card-front .brand-bar { height: 5px; }
  .holder { position: absolute; left: 116px; top: 54px; }
  .holder-name { font-size: 7.5px; font-weight: 600; color: var(--brand-blue); line-height: 8px; }
  .holder-role { font-size: 4.5px; color: var(--ink-soft); }
  .card-front .contact { left: 116px; top: 74px; font-size: 5px; line-height: 6.4px; }

  /* Business card back */
  .card-back { left: 106px; top: 471px; width: 221px; height: 126px; background: var(--charcoal); }
  .card-back .wordmark { left: 50%; top: 52px; transform: translateX(-50%); font-size: 17px; }
  .card-back .site { position: absolute; left: 0; right: 0; top: 90px; text-align: center; font-size: 5px; color: #dddddd; letter-spacing: .03em; }

  /* Letterhead */
  .letterhead { left: 351px; top: 63px; width: 377px; height: 534px; }
  .letterhead .wordmark { left: 40px; top: 33px; font-size: 20px; }
  .letterhead .contact--address { left: 252px; top: 41px; }
  .letterhead .contact--reach { left: 305px; top: 41px; }
  .letterhead .brand-bar { height: 6px; }
  .letter { position: absolute; left: 72px; width: 274px; font-size: 6.4px; line-height: 8.4px; color: var(--ink); }
  .recipient { top: 134px; }
  .recipient strong, .signature strong { font-weight: 600; }
  .letter-body { top: 196px; text-align: justify; }
  .letter-body p { margin-bottom: 8.4px; }
  .signature { top: 399px; }
  .legal { position: absolute; right: 70px; bottom: 10px; font-size: 3.4px; color: var(--ink-soft); }

  /* Compliment slip */
  .comp-slip { left: 748px; top: 408px; width: 341px; height: 186px; }
  .comp-slip .greeting { position: absolute; left: 34px; top: 14px; font-family: var(--script); font-style: italic; font-weight: 500; font-size: 17px; color: var(--ink-soft); }
  .comp-slip .wordmark { left: 113px; top: 158px; font-size: 15px; }
  .comp-slip .contact--address { left: 182px; top: 164px; }
  .comp-slip .contact--reach { left: 233px; top: 164px; }
  .comp-slip .brand-bar { height: 6px; }
</style>
</head>
<body>

  <!-- Business card, front -->
  <section class="sheet card-front" aria-label="Business card front">
    <div class="wordmark">VORN-Q<span class="mark-square"></span></div>
    <div class="holder">
      <p class="holder-name">Dan Myles</p>
      <p class="holder-role">Director</p>
    </div>
    <div class="contact">
      <div class="contact-row">
        <svg width="4" height="5" viewBox="0 0 10 13"><path d="M5 0a5 5 0 0 0-5 5c0 3.6 5 8 5 8s5-4.4 5-8a5 5 0 0 0-5-5zm0 7a2 2 0 1 1 0-4 2 2 0 0 1 0 4z" fill="var(--brand-blue)"/></svg>
        <span>62-74 Marrow Lane<br>London N7 3QT</span>
      </div>
      <div class="contact-row">
        <svg width="4" height="5" viewBox="0 0 10 10"><path d="M2 0l2 2.5-1.2 1.5a6 6 0 0 0 3.2 3.2L7.5 6 10 8 8.5 10C4 10 0 6 0 1.5z" fill="var(--brand-blue)"/></svg>
        <span>020 7195 8843</span>
      </div>
      <div class="contact-row">
        <svg width="4" height="5" viewBox="0 0 10 10"><circle cx="5" cy="5" r="5" fill="var(--brand-blue)"/><path d="M2.5 3.5h5v3h-5z" fill="#fff"/></svg>
        <span>dan@vorn-q.co</span>
      </div>
    </div>
    <div class="brand-bar"><span class="bar-dark"></span><span class="bar-blue"></span><span class="bar-green"></span></div>
  </section>

  <!-- Business card, back -->
  <section class="sheet card-back" aria-label="Business card back">
    <div class="wordmark wordmark--light">VORN-Q<span class="mark-square"></span></div>
    <p class="site">www.vorn-q.co</p>
  </section>

  <!-- Letterhead -->
  <section class="sheet letterhead" aria-label="Letterhead">
    <div class="wordmark">VORN-Q<span class="mark-square"></span></div>
    <div class="contact contact--address">
      <div class="contact-row">
        <svg width="4" height="5" viewBox="0 0 10 13"><path d="M5 0a5 5 0 0 0-5 5c0 3.6 5 8 5 8s5-4.4 5-8a5 5 0 0 0-5-5zm0 7a2 2 0 1 1 0-4 2 2 0 0 1 0 4z" fill="var(--brand-blue)"/></svg>
        <span>62-74 Marrow Lane<br>London N7 3QT</span>
      </div>
    </div>
    <div class="contact contact--reach">
      <div class="contact-row">
        <svg width="4" height="4" viewBox="0 0 10 10"><path d="M2 0l2 2.5-1.2 1.5a6 6 0 0 0 3.2 3.2L7.5 6 10 8 8.5 10C4 10 0 6 0 1.5z" fill="var(--brand-blue)"/></svg>
        <span>020 7195 8843</span>
      </div>
      <div class="contact-row">
        <svg width="4" height="4" viewBox="0 0 10 10"><circle cx="5" cy="5" r="4.3" fill="none" stroke="var(--brand-blue)" stroke-width="1.4"/><path d="M.7 5h8.6M5 .7c2.4 2.4 2.4 6.2 0 8.6M5 .7c-2.4 2.4-2.4 6.2 0 8.6" fill="none" stroke="var(--brand-blue)" stroke-width="1"/></svg>
        <span>www.vorn-q.co</span>
      </div>
    </div>

    <div class="letter recipient">
      <strong>Mr. Owen Hartley</strong><br>
      Managing Director<br>
      Northgate Investor<br>
      28 W Harbor Road<br>
      USA
    </div>

    <div class="letter letter-body">
      <p>Lorem Ipsum is simply dummy text for printing and typesetting industry. Lorem Ipsum has been the industry's standard dummy text since the 1500s, when an unknown printer galley of type and scrambled it to make a type specimen book. It has suvived not only manual but also the leap into electronic typesetting, remaining essentially un changed. It was popularised in the 1960s with the release of Printaline sheets containing Lorem Ipsum pass and more recently with desktop publishing software like Pagecraft Studio including version 6.9 of Lorem Ipsum.</p>
      <p>Country to popular belief, Lorem Ipsum is not simply random text. It has roots in a piece of sical Latin literature from 45 BC, making it over 2000 years old. Peter Aldwin, a prfessor at Elmbrook College in Virginia, looked up one of the most of the world classical literature, discovered the undoubtable sorce. Lorem Ipsum comes from section 1.10.32 and 1.10.33 of "de Finibus Bonorum et Molorum" ( The Extreme of Good and Even Tullio), written in 45 BC. This book is a treatise on the theory of ethics very popular during Renassiance.</p>
      <p>Thank you for being one of our valued customers.</p>
    </div>

    <div class="letter signature">
      <strong>Dan Myles</strong><br>
      Director
    </div>

    <p class="legal">Company is Registered in England and Wales Company No. 06412853</p>
    <div class="brand-bar"><span class="bar-dark"></span><span class="bar-blue"></span><span class="bar-green"></span></div>
  </section>

  <!-- Compliment slip -->
  <section class="sheet comp-slip" aria-label="Compliment slip">
    <p class="greeting">with compliments</p>
    <div class="wordmark">VORN-Q<span class="mark-square"></span></div>
    <div class="contact contact--address">
      <div class="contact-row">
        <svg width="4" height="5" viewBox="0 0 10 13"><path d="M5 0a5 5 0 0 0-5 5c0 3.6 5 8 5 8s5-4.4 5-8a5 5 0 0 0-5-5zm0 7a2 2 0 1 1 0-4 2 2 0 0 1 0 4z" fill="var(--brand-blue)"/></svg>
        <span>62-74 Marrow Lane<br>London N7 3QT</span>
      </div>
    </div>
    <div class="contact contact--reach">
      <div class="contact-row">
        <svg width="4" height="4" viewBox="0 0 10 10"><path d="M2 0l2 2.5-1.2 1.5a6 6 0 0 0 3.2 3.2L7.5 6 10 8 8.5 10C4 10 0 6 0 1.5z" fill="var(--brand-blue)"/></svg>
        <span>020 7195 8843</span>
      </div>
      <div class="contact-row">
        <svg width="4" height="4" viewBox="0 0 10 10"><circle cx="5" cy="5" r="4.3" fill="none" stroke="var(--brand-blue)" stroke-width="1.4"/><path d="M.7 5h8.6M5 .7c2.4 2.4 2.4 6.2 0 8.6M5 .7c-2.4 2.4-2.4 6.2 0 8.6" fill="none" stroke="var(--brand-blue)" stroke-width="1"/></svg>
        <span>www.vorn-q.co</span>
      </div>
    </div>
    <div class="brand-bar"><span class="bar-dark"></span><span class="bar-blue"></span><span class="bar-green"></span></div>
  </section>

</body>
</html>
```